Book Cover Design - Uncovering Weight Loss Secrets

I need a book cover design for a book called 'Folding The Map'. It is a book that goes through all of the secrets to weight loss, without any crazy shakes or workouts or pills or potions. The book is really focused on helping people understand that Weight loss is simple and has more to do with our mindset as well as the food we were eating. It is about taking personal responsibility not looking for the next fancy revolutionary product that is going to help them magically melt the fat away. The book is pragmatic in nature and breaks down in simple terms how we can lose weight and keep it off for the rest of our lives. It shows the user that it is simple to lose weight, but it takes effort. They should stop looking for a quick fix when it comes to weight loss but instead eat healthy for the rest of their lives.
The book is intended to be hard-hitting no holds barred approach. The book has the same title as my business name. I will attach the current logo that we use in the business. This doesn't need to be on the front of the book maybe at the back down the bottom somewhere.
I am looking to have both an e-book cover and a standard printed book cover.
I don't have any colours in mind, my logo can be adapted to be different colours or just white.
The message that I am wanting people to feel when they see my book, is that all these Weightloss fads are a joke, that I know the secrets that will get them to their weight loss goal even if they fail at everything else before.
On the cover it should say the following.
FOLDING THE MAP
Uncovering the Weight Loss Secrets
The big companies have been trying to keep hidden for years!
COLIN MAYHEW
People who have failed many times trying to lose weight & need help
Weight Loss

```html
<!DOCTYPE html>
<html lang="en">
<head>
<meta charset="utf-8">
<title>Folding The Map — Colin Mayhew</title>
<link rel="stylesheet" href="https://fonts.googleapis.com/css2?family=Oswald:wght@400;700&display=swap">
<style>
  :root {
    --cover-black: #000000;
    --author-white: #ffffff;
    --gold-light: #fff38c;
    --gold-mid: #f0cf63;
    --gold-deep: #bf8639;
    --silver-light: #ffffff;
    --silver-mid: #8a8a8a;
    --glow-gold: #e0b24a;
    --glow-dark: #2a1d08;
  }
  html, body {
    margin: 0;
    padding: 0;
    width: 800px;
    height: 1200px;
    overflow: hidden;
    background: var(--cover-black);
  }
  .book-cover {
    display: block;
    width: 800px;
    height: 1200px;
  }
  .author-name {
    font-family: "Oswald", sans-serif;
    font-weight: 700;
    font-size: 57px;
    fill: var(--author-white);
    letter-spacing: 1px;
  }
  .title-line {
    font-family: "Oswald", sans-serif;
    font-weight: 700;
    font-size: 192px;
  }
  .subtitle-lead {
    font-family: "Oswald", sans-serif;
    font-weight: 400;
    font-size: 68px;
  }
  .subtitle-line {
    font-family: "Oswald", sans-serif;
    font-weight: 400;
    font-size: 56px;
  }
  .tagline-line {
    font-family: "Oswald", sans-serif;
    font-weight: 400;
    font-size: 56px;
  }
</style>
</head>
<body>
<svg class="book-cover" viewBox="0 0 800 1200" xmlns="http://www.w3.org/2000/svg">
  <defs>
    <linearGradient id="gold-metal" x1="0" y1="0" x2="0" y2="1">
      <stop offset="0.18" stop-color="var(--gold-light)"/>
      <stop offset="0.42" stop-color="var(--gold-mid)"/>
      <stop offset="0.58" stop-color="var(--gold-deep)"/>
      <stop offset="0.78" stop-color="var(--gold-mid)"/>
      <stop offset="1" stop-color="var(--gold-light)"/>
    </linearGradient>
    <linearGradient id="silver-metal" x1="0" y1="0" x2="0" y2="1">
      <stop offset="0.2" stop-color="var(--silver-light)"/>
      <stop offset="0.62" stop-color="var(--silver-light)"/>
      <stop offset="0.8" stop-color="var(--silver-mid)"/>
      <stop offset="1" stop-color="var(--silver-light)"/>
    </linearGradient>
    <radialGradient id="apple-glow" cx="0.5" cy="0.55" r="0.5">
      <stop offset="0" stop-color="var(--glow-gold)"/>
      <stop offset="0.45" stop-color="#8a6524"/>
      <stop offset="0.8" stop-color="var(--glow-dark)"/>
      <stop offset="1" stop-color="var(--cover-black)"/>
    </radialGradient>
  </defs>

  <rect class="cover-background" width="800" height="1200" fill="var(--cover-black)"/>

  <text class="author-name" x="400" y="85" text-anchor="middle">COLIN MAYHEW</text>

  <g class="book-title" fill="url(#gold-metal)" text-anchor="middle">
    <text class="title-line" x="400" y="303">FOLDING</text>
    <text class="title-line" x="400" y="490">THE MAP</text>
  </g>

  <g class="book-subtitle" fill="url(#silver-metal)" text-anchor="middle">
    <text class="subtitle-lead" x="400" y="580">UNCOVERING</text>
    <text class="subtitle-line" x="400" y="647">THE WEIGHT LOSS SECRETS</text>
  </g>

  <ellipse class="cover-illustration" cx="400" cy="850" rx="200" ry="175"
           fill="url(#apple-glow)" role="img"
           aria-label="Glowing golden apple with a leaf and a keyhole cut into its front"/>

  <g class="book-tagline" fill="url(#silver-metal)" text-anchor="middle">
    <text class="tagline-line" x="400" y="1097">THE BIG COMPANIES HAVE BEEN</text>
    <text class="tagline-line" x="400" y="1150">TRYING TO KEEP HIDDEN FOR YEARS!</text>
  </g>
</svg>
</body>
</html>
```